Author Personal Brand Wordpress Design

I need a wordpress theme to rebrand my website. I am an author who writes both romance and fantasy novels and therefore want a brand that will represent my style of writing which is warm, emotional and adventurous.

My name should be across the top (Maren Holt). Font used should be modern, easy-to-read and fun. My preference is towards handwritten fonts, but this is not essential.

Colours should be cheerful, vibrant and light (no dark backgrounds please) - maybe reds and yellows (but not essential - use your imagination). Images can be used.

The final design should communicate approachable, warm and positive.

The designers should keep in mind that elements of the final design should be able to be incorporated into a stationery suite (letterhead, business cards, email signature, powerpoint and with compliments slip) and the header should be able to be resized for an email newsletter (PostLark), and Chirply/Frendbook.

The website design must be responsive, and take the full width of the page (see the Pellucid theme or Driftwick theme for an example of what I mean). Social media icons must be able to be installed and used and the menu should run horizontally across the page. My preference is to be able to have multiple sidebars (one for blog and one for the rest of the site), and a sticky menu.

I need to be able to install the design into Wordpress and I can create additional pages from there. See my current website www.marenholt-example.com for examples of content.

Final Product:
- Wordpress web design I can install myself
- Header image which can be resized for newsletter, Frendbook and Chirply
- Name of font used (must be one I have access to eg: can purchase)
- List of colours used

Target Market(s)

Women 25-50

Industry/Entity Type

Business

Requirements
Must have
• Responsive, full width, social media icons (preferably at the top of the page)
Nice to have
• Sticky menu, accessibility
Should not have
• No couples embracing, or holding hands. The design should not be about the romance genre as I will be writing fantasy this year.

```html
<!DOCTYPE html>
<html lang="en">
<head>
<meta charset="utf-8">
<title>Maren Holt – Author</title>
<link rel="stylesheet" href="https://fonts.googleapis.com/css2?family=Great+Vibes&family=Parisienne&family=Dancing+Script:wght@400;600&family=Open+Sans:wght@400;600&display=swap">
<style>
:root{
  --red:#b8121d;
  --red-dark:#9c0e17;
  --red-deep:#8c0c14;
  --nav-top:#c81a24;
  --nav-bottom:#a80f18;
  --paper:#f5f3f3;
  --card:#ffffff;
  --frame:#e4e2e2;
  --line:#d6d2d2;
  --text:#555152;
  --text-soft:#777;
  --orange:#f36d2b;
  --white:#ffffff;
}
*{margin:0;padding:0;box-sizing:border-box}
html,body{width:1200px;height:2400px;overflow:hidden}
body{position:relative;background:var(--paper);font-family:"Open Sans",Arial,sans-serif;color:var(--text)}
.abs{position:absolute}
.script{font-family:"Parisienne",cursive;font-weight:400}

/* header */
.site-header{top:0;left:0;width:1200px;height:133px;background:var(--white);display:flex;align-items:center;justify-content:center;gap:14px}
.brand-name{font-family:"Great Vibes",cursive;font-size:74px;color:var(--red);line-height:1}
.brand-mark{width:26px;height:26px;border-radius:50%;background:var(--red);margin-top:-20px}

.main-nav{top:133px;left:0;width:1200px;height:54px;background:linear-gradient(var(--nav-top),var(--nav-bottom));display:flex;justify-content:center}
.main-nav a{font-family:"Parisienne",cursive;color:var(--white);text-decoration:none;font-size:25px;line-height:54px;padding:0 25px;border-left:1px solid rgba(255,255,255,.15);border-right:1px solid rgba(0,0,0,.12)}

/* slider */
.slider{top:211px;left:147px;width:906px;height:384px;background:linear-gradient(#f2f1f1,#dcdada);border-radius:8px;box-shadow:0 14px 18px -8px rgba(0,0,0,.25)}
.slide{top:16px;left:16px;width:874px;height:339px;border-radius:6px;background:linear-gradient(100deg,#8aa15c 0%,#5f7a3a 35%,#c8a98c 62%,#6c4a34 82%,#3a2a20 100%)}
.slide-title{top:105px;left:34px;font-family:"Great Vibes",cursive;color:var(--white);font-size:78px;line-height:1;text-shadow:0 2px 6px rgba(0,0,0,.35)}
.slide-sub{top:180px;left:34px;font-family:"Great Vibes",cursive;color:var(--white);font-size:44px;text-shadow:0 2px 6px rgba(0,0,0,.35)}
.slide-arrows{top:313px;left:808px;display:flex;gap:3px}
.slide-arrows span{width:25px;height:26px;background:var(--red);display:flex;align-items:center;justify-content:center}
.ribbon{top:-2px;left:-8px;width:110px;height:110px;overflow:hidden}
.ribbon span{position:absolute;top:30px;left:-34px;width:150px;transform:rotate(-45deg);background:var(--red);color:var(--white);font-size:8px;font-weight:600;text-align:center;line-height:20px;letter-spacing:.3px}
.slide-dots{top:352px;left:375px;width:112px;height:29px;background:linear-gradient(#fafafa,#dedcdc);border-radius:4px;display:flex;gap:6px;align-items:center;justify-content:center}
.slide-dots i{width:9px;height:9px;border-radius:50%;background:#bbb;display:block}
.slide-dots i:first-child{background:#777}

/* section headings */
.section-title{left:258px;width:684px;display:flex;align-items:center;gap:14px;color:var(--red);font-size:42px;font-family:"Parisienne",cursive;white-space:nowrap}
.section-title::before,.section-title::after{content:"";flex:1;height:5px;border-top:1px solid var(--line);border-bottom:1px solid var(--line)}

.welcome{top:700px;left:185px;width:830px;text-align:center;font-size:12.5px;line-height:23px}
.welcome p{margin-bottom:22px}

/* features */
.feature{top:909px;width:290px;text-align:center}
.ring{border-radius:50%;background:var(--white);box-shadow:0 0 0 1px #e2dede,0 3px 6px rgba(0,0,0,.08);display:flex;align-items:center;justify-content:center;margin:0 auto}
.ring .photo{border-radius:50%}
.feature .ring{width:170px;height:170px}
.feature .photo{width:150px;height:150px}
.feature h3{font-family:"Parisienne",cursive;font-weight:400;color:var(--red);font-size:40px;margin-top:10px;line-height:1.2}
.feature p{font-size:12.5px;line-height:23px;margin-top:6px}

/* events */
.event{top:1325px;width:440px;display:flex;gap:26px}
.event .ring{width:157px;height:157px;flex:none;margin:0}
.event .photo{width:138px;height:138px}
.event h4{font-family:"Parisienne",cursive;font-weight:400;color:var(--red);font-size:28px;margin-top:10px}
.event .date{font-family:"Dancing Script",cursive;color:var(--red);font-size:15px;margin-top:2px}
.event p{font-family:"Dancing Script",cursive;font-size:16px;line-height:24px;color:var(--text);margin-top:6px}

/* about */
.about{top:1528px;left:147px;width:906px;height:243px;background:#efeded;border:1px solid #e2dfdf;padding:8px}
.about-inner{width:100%;height:100%;border:1px solid #dedada;position:relative}
.about .ring{position:absolute;left:20px;top:20px;width:182px;height:182px}
.about .photo{width:160px;height:160px}
.about h3{position:absolute;left:234px;top:16px;font-family:"Parisienne",cursive;font-weight:400;color:var(--red);font-size:38px}
.about p{position:absolute;left:234px;top:74px;width:640px;font-family:"Dancing Script",cursive;font-size:16px;line-height:26px}
.btn-more{position:absolute;left:234px;top:161px;width:135px;height:35px;background:var(--red);color:var(--white);font-family:"Parisienne",cursive;font-size:21px;line-height:35px;text-align:center;border-radius:2px}

/* books */
.books{top:1870px;left:147px;width:906px;display:flex;justify-content:space-between}
.book{width:216px;height:282px;background:var(--card);border:1px solid #dcd8d8;text-align:center;padding-top:22px}
.book .cover{width:123px;height:189px;margin:0 auto}
.book h5{font-weight:400;font-size:16px;color:#333;margin-top:9px}
.book small{display:block;font-size:10.5px;color:var(--text-soft);margin-top:3px}

/* newsletter */
.newsletter{top:2202px;left:0;width:1200px;height:67px;background:var(--red);display:flex;align-items:center;padding-left:202px}
.newsletter label{font-family:"Parisienne",cursive;color:var(--white);font-size:27px;width:388px}
.newsletter .field{width:298px;height:31px;background:var(--white);border-radius:2px;font-size:10px;color:#999;line-height:31px;padding-left:14px}
.newsletter .submit{margin-left:11px;width:99px;height:31px;background:linear-gradient(#f7874a,var(--orange));color:var(--white);font-family:"Parisienne",cursive;font-size:20px;text-align:center;line-height:31px;border-radius:2px}

/* footer */
.site-footer{top:2269px;left:0;width:1200px;height:131px;background:var(--red-deep)}
.footer-links{position:absolute;left:147px;top:40px;display:flex;font-size:12px;color:var(--white)}
.footer-links span.sep{margin:0 16px}
.copyright{position:absolute;left:147px;top:73px;font-size:12px;color:var(--white)}
.copyright span{margin:0 10px}
.social{position:absolute;right:147px;top:58px;display:flex;gap:14px;font-size:12px;color:var(--white);align-items:center}
.social li{list-style:none;display:flex;align-items:center;gap:5px}
.social li::before{content:"";width:14px;height:14px;border-radius:50%;background:var(--white)}
</style>
</head>
<body>

<header class="site-header abs">
  <span class="brand-name">Maren Holt</span>
  <span class="brand-mark"></span>
</header>

<nav class="main-nav abs">
  <a href="#">Home</a><a href="#">Bio</a><a href="#">Books</a><a href="#">Events</a><a href="#">Memberships</a><a href="#">Resources</a><a href="#">Contact</a><a href="#">Media</a>
</nav>

<section class="slider abs">
  <div class="slide abs" role="img" aria-label="Photo of a young woman reading a book outdoors under trees">
    <div class="slide-title abs">Maren Holt</div>
    <div class="slide-sub abs">Modern Romance</div>
    <div class="slide-arrows abs">
      <span><svg width="8" height="12" viewBox="0 0 8 12"><path d="M6 1 1 6l5 5" fill="none" stroke="#fff" stroke-width="2"/></svg></span>
      <span><svg width="8" height="12" viewBox="0 0 8 12"><path d="M2 1l5 5-5 5" fill="none" stroke="#fff" stroke-width="2"/></svg></span>
    </div>
  </div>
  <div class="ribbon abs"><span>MODERN ROMANCE</span></div>
  <div class="slide-dots abs"><i></i><i></i><i></i><i></i><i></i></div>
</section>

<h2 class="section-title abs" style="top:630px">Welcome to Maren Holt</h2>
<div class="welcome abs">
  <p>I'm a romance author, board game fanatic and sidecar swinger. I love to try new things which is how I ended up hanging off the side of a vintage moto-cross sidecar. Hmmm, not one of my safest ideas although it is fun.</p>
  <p>Details of my debut book can be found on the Books page.</p>
  <p>I attend a monthly critique group which is the main reason my writing has improved so much since I started. See the Memberships section for details of my talented group. Most of us started off unpublished and now we all have published novels available.</p>
</div>

<article class="feature abs" style="left:133px">
  <div class="ring"><div class="photo" role="img" aria-label="Photo of two people at sunset" style="background:radial-gradient(circle at 50% 35%,#f4c25a,#c9702a 55%,#3b2416)"></div></div>
  <h3>Memberships</h3>
  <p>I'm a romance author, board game fanatic and sidecar swinger. I love to try new things which is how I ended up hanging...</p>
</article>
<article class="feature abs" style="left:455px">
  <div class="ring"><div class="photo" role="img" aria-label="Photo of a hand writing with a pen" style="background:radial-gradient(circle at 45% 45%,#d8d8d8,#6e6e6e 55%,#1e1e1e)"></div></div>
  <h3>Resources</h3>
  <p>I'm a romance author, board game fanatic and sidecar swinger. I love to try new things which is how I ended up hanging...</p>
</article>
<article class="feature abs" style="left:777px">
  <div class="ring"><div class="photo" role="img" aria-label="Photo of silhouettes against an evening sky" style="background:linear-gradient(#cfe0f0,#e8c88a 55%,#2a2218 70%)"></div></div>
  <h3>Media</h3>
  <p>I'm a romance author, board game fanatic and sidecar swinger. I love to try new things which is how I ended up hanging...</p>
</article>

<h2 class="section-title abs" style="top:1244px">Latest Events</h2>

<article class="event abs" style="left:143px">
  <div class="ring"><div class="photo" role="img" aria-label="Photo of a swirling colourful tunnel" style="background:radial-gradient(circle,#e0a56a,#7a3b55 50%,#2a2040)"></div></div>
  <div>
    <h4>Guild Book Signing</h4>
    <div class="date">09 August 2014</div>
    <p>I was at the Lantern Story Readers Guild book-signing event in Sydney in August. It was held in conjunction...</p>
  </div>
</article>
<article class="event abs" style="left:607px">
  <div class="ring"><div class="photo" role="img" aria-label="Photo of a fountain pen on handwritten paper" style="background:radial-gradient(circle at 40% 40%,#efe6d6,#b9a486 60%,#6e5a40)"></div></div>
  <div>
    <h4>Guild Book Signing</h4>
    <div class="date">09 August 2014</div>
    <p>I was at the Lantern Story Readers Guild book-signing event in Sydney in August. It was held in conjunction...</p>
  </div>
</article>

<section class="about abs">
  <div class="about-inner">
    <div class="ring"><div class="photo" role="img" aria-label="Portrait photo of the author" style="background:radial-gradient(circle at 50% 40%,#f0c8a8,#b5583a 55%,#3aa6c8)"></div></div>
    <h3>About me</h3>
    <p>I was a voracious reader as a child, devouring anything by Edna Whitlow as well as series such as Nell Darby, Tessa Bellweather, The Sitters Circle and Willow Creek High. Then one school holidays when I'd run out of books to read, my mum handed me 'Cold Fire' by Nola Rivers and I instantly fell in love with romance novels.</p>
    <div class="btn-more">Read More</div>
  </div>
</section>

<h2 class="section-title abs" style="top:1796px">Futured books</h2>

<section class="books abs">
  <div class="book"><div class="cover" role="img" aria-label="Photo of a carved stone warrior statue" style="background:linear-gradient(#c9b8a4,#7a634c)"></div><h5>Book Tittle here</h5><small>lit Integer congue augue et malesuada</small></div>
  <div class="book"><div class="cover" role="img" aria-label="Photo of a pocket watch among old books" style="background:linear-gradient(#4a3a2a,#c9a46a 55%,#5a4030)"></div><h5>Book Tittle here</h5><small>lit Integer congue augue et malesuada</small></div>
  <div class="book"><div class="cover" role="img" aria-label="Photo of hands shaping clay" style="background:linear-gradient(#3a2418,#a8603a 60%,#4a2c1c)"></div><h5>Book Tittle here</h5><small>lit Integer congue augue et malesuada</small></div>
  <div class="book"><div class="cover" role="img" aria-label="Book cover with a misty tree-lined path" style="background:linear-gradient(#2e3a30,#6a7a68 60%,#2a302a)"></div><h5>Book Tittle here</h5><small>lit Integer congue augue et malesuada</small></div>
</section>

<section class="newsletter abs">
  <label>Subscribe to our Newsletter to be noted</label>
  <div class="field">Enter your email id...</div>
  <div class="submit">Submit</div>
</section>

<footer class="site-footer abs">
  <div class="footer-links">
    <span>Home</span><span class="sep">/</span><span>Bio</span><span class="sep">/</span><span>Books</span><span class="sep">/</span><span>Events</span><span class="sep">/</span><span>Memberships</span><span class="sep">/</span><span>Resources</span><span class="sep">/</span><span>Contact</span><span class="sep">/</span><span>Media</span>
  </div>
  <div class="copyright">Copyright © 2014. Maren Holt. All rights reserved. Privacy Policy<span>|</span>Terms of Use</div>
  <ul class="social">
    <li>Frendbook</li><li>Chirply</li><li>Linkwise</li><li>Feed</li>
  </ul>
</footer>

</body>
</html>
```